Web Design Project (Renewable Energy Services Company)

Hello crowd,

We are looking to create a website for a new company. We would like to have the page already coded, if you do not provide the code as well, please indicate so. I am including a very preliminary approximation of the wireframe.

We do not have the logo either the color pallet, however we have in mind couple websites that would be similar tho these.

http://www.brivolen.com/en/

and

http://www.tarmuvex.com/

We did an approximated wireframe our our website, not necesarly to decide on the layout but rather to know how many pages will be needed. It would be around 10 pages. We will need a section that will be an e-commerce page to sell products such as engineering instrumentation, software and consumables such as cable and connectors.

Our company will be called ORVIK. We will be based in Monterrey, Mexico. Our focused will be the development of renewable energy projects. Similar scope of services than http://www.brivolen.com/en/ but only for wind and solar projects.

We like something minimalistic. Some of the things that the logo might or might not include would be the monterrey famous hill, but not strictly necessary.
http://en.plavorinet.org/wiki/Loma_del_Trueno

also ORVIK (which stands for ORganica VIKtoria) the name is similar the bird (seagal) or wind turbines and sun...any of these are only suggestions and we are open to receive any proposals.

There must be a
home page
services page (some subsections)
products page (some subsections)
contact page with contact form

and some additional subsections like careers and partnerships.

We are very excited to start hearing about this project.
Updates

Please for the logo, do not restrict your ideas to the ones provided as it has generated too specific logos. Pleae just allow your imagination to flow for a company that develops renewable energy projects.

Target Market(s)

large companies interested in developing renewable energy projects

Industry/Entity Type

E-Commerce

Requirements
Must have
• Minimalistic and unique design.
Nice to have
• contact form to save contacts in a database

Should not have
• We are looking a very minimalistic logo. It should not be an explicit wind turbine a seagal or anything like that. we are looking for abstract, simple and minimalistic image.

```html
<!DOCTYPE html>
<html lang="es">
<head>
<meta charset="utf-8">
<title>ORVIK – Proyectos Renovables</title>
<link href="https://fonts.googleapis.com/css2?family=PT+Sans:wght@400;700&display=swap" rel="stylesheet">
<style>
:root{
  --brand-red:#c4302f;
  --hero-red:#c8403f;
  --hero-red-dark:#b93433;
  --tab-pink:#f4a19e;
  --ink-dark:#333333;
  --footer-bg:#4a4a4a;
  --page-top:#efefef;
  --page-bg:#ffffff;
  --muted:#999999;
  --white:#ffffff;
  --photo-blue:#3f7dc6;
  --photo-light:#8db8e2;
}
*{margin:0;padding:0;box-sizing:border-box}
html,body{width:1200px;height:872px;overflow:hidden}
body{
  position:relative;
  font-family:"PT Sans",Arial,sans-serif;
  background:linear-gradient(180deg,var(--page-top) 0,var(--page-bg) 110px,var(--page-bg) 100%);
}
.brand{position:absolute;left:18px;top:60px;display:flex;align-items:center;gap:14px}
.brand-mark{width:34px;height:34px;border-radius:50%;background:var(--ink-dark)}
.brand-name{font-size:52px;line-height:1;color:var(--brand-red);font-weight:400;letter-spacing:1px}
.checkout{
  position:absolute;left:1049px;top:35px;width:133px;height:28px;border-radius:3px;
  background:var(--ink-dark);color:var(--white);font-size:14px;
  display:flex;align-items:center;justify-content:center;gap:8px;
}
.search{
  position:absolute;left:991px;top:78px;width:191px;height:29px;border:1px solid #d4d4d4;
  border-radius:3px;background:var(--white);box-shadow:inset 0 1px 2px rgba(0,0,0,.1);
  font-size:13px;font-style:italic;color:var(--muted);padding:6px 12px;
}
.search svg{position:absolute;right:8px;top:8px}
.main-nav{position:absolute;left:34px;top:144px;height:46px;display:flex;align-items:center;font-size:17px;color:var(--brand-red)}
.main-nav a{color:inherit;text-decoration:none;padding:0 16px}
.main-nav .sep{padding:0 12px}
.main-nav .current{background:var(--brand-red);color:var(--white);height:46px;display:flex;align-items:center;border-radius:3px 3px 0 0;padding:0 16px}
.hero{
  position:absolute;left:18px;top:191px;width:1162px;height:512px;border-radius:3px;overflow:hidden;
  background:radial-gradient(ellipse at 90% 30%,#d65a58 0,var(--hero-red) 40%,var(--hero-red-dark) 100%);
}
.hero-title{position:absolute;left:81px;top:19px;color:var(--white);font-size:27px;font-weight:400;line-height:31px}
.hero-title span{display:block}
.hero-title span + span{padding-left:195px}
.hero-photo{
  position:absolute;left:24px;top:101px;width:694px;height:363px;border:5px solid var(--white);border-radius:8px;
  background:linear-gradient(160deg,var(--photo-blue) 0,var(--photo-light) 100%);
  box-shadow:0 6px 10px rgba(0,0,0,.25);
}
.slider-dots{position:absolute;left:311px;top:480px;display:flex;gap:18px;align-items:center}
.slider-dots i{width:12px;height:12px;border-radius:50%;background:#e8e8e8;display:block}
.slider-dots i.active{width:16px;height:16px;background:var(--ink-dark);border:2px solid #e8e8e8}
.service-list{position:absolute;left:742px;top:113px;width:395px;list-style:none;color:var(--white);font-size:16.5px;line-height:20.4px}
.service-list li{position:relative;padding-left:26px;margin-bottom:13.2px}
.service-list li::before{content:"›";position:absolute;left:2px;top:-2px;font-size:20px;font-weight:700}
.energy-tabs{
  position:absolute;left:908px;top:474px;width:226px;height:38px;background:var(--tab-pink);
  border-radius:3px 3px 0 0;color:var(--ink-dark);font-size:15px;display:flex;align-items:center;justify-content:center;gap:10px;
}
.site-footer{
  position:absolute;left:18px;top:719px;width:1162px;height:128px;border-radius:3px;background:var(--footer-bg);
  color:var(--white);font-size:15px;
}
.footer-links{position:absolute;left:26px;top:32px}
.footer-links .sep{padding:0 8px}
.copyright{position:absolute;left:26px;top:68px}
.address{position:absolute;left:844px;top:32px;line-height:34px;font-style:normal}
.mail-icon{position:absolute;left:1084px;top:37px}
</style>
</head>
<body>
<header>
  <div class="brand"><span class="brand-mark"></span><span class="brand-name">ORVIK</span></div>
  <div class="checkout">
    <svg width="20" height="16" viewBox="0 0 20 16" aria-hidden="true"><path d="M1 2h3l3 8h9l2-6H6" fill="none" stroke="#fff" stroke-width="1.6"/><circle cx="8" cy="13.5" r="1.5" fill="#fff"/><circle cx="15" cy="13.5" r="1.5" fill="#fff"/></svg>
    CHECK OUT
  </div>
  <div class="search">Search
    <svg width="12" height="12" viewBox="0 0 12 12" aria-hidden="true"><circle cx="5" cy="5" r="3.5" fill="none" stroke="#aaa" stroke-width="1.4"/><path d="M7.5 7.5l3.5 3.5" stroke="#aaa" stroke-width="1.6"/></svg>
  </div>
  <nav class="main-nav">
    <a class="current">Inicio</a><span class="sep">|</span>
    <a>Servicios</a><span class="sep">|</span>
    <a>Productos</a><span class="sep">|</span>
    <a>Nuestra Especialidad</a><span class="sep">|</span>
    <a>Contacto</a>
  </nav>
</header>
<main class="hero">
  <h1 class="hero-title"><span>Proyectos Renovables</span><span>para Mexico y Latino America</span></h1>
  <div class="hero-photo" role="img" aria-label="Photo: wind turbines in a green field under a blue sky"></div>
  <div class="slider-dots"><i></i><i></i><i class="active"></i><i></i><i></i></div>
  <ul class="service-list">
    <li>Energia Eolica</li>
    <li>Proyectos de Generacion Eolica desde 1MW hasta 200 MV</li>
    <li>Analisis Detallado de Recurso Eolico</li>
    <li>Diseno de Parques Eolicos</li>
    <li>Permitologia</li>
    <li>Consejo Nacional de Redes CNR</li>
    <li>SEMARVEN</li>
    <li>CRV</li>
    <li>Analisis de Riesgo y Factibilidad Financiera</li>
    <li>PPA and Tariff Analysis</li>
  </ul>
  <div class="energy-tabs"><span>Energia Eolica</span><span>|</span><span>Energia Solar</span></div>
</main>
<footer class="site-footer">
  <div class="footer-links">Carreras<span class="sep">|</span>Quienes Somos</div>
  <div class="copyright">Copyright © 2012 www.orvik.com</div>
  <address class="address">Calle Brisas 215, Col. Valle Alto<br>Monterrey, N.L. 64870</address>
  <svg class="mail-icon" width="50" height="42" viewBox="0 0 50 42" aria-hidden="true">
    <path d="M4 12l30-10 12 24-30 12z" fill="#f2f2f2"/>
    <path d="M4 12l22 10 20 4" fill="none" stroke="#cfcfcf" stroke-width="1.2"/>
    <path d="M14 22l16-6 4 8-16 6z" fill="#3d7fc4"/>
  </svg>
</footer>
</body>
</html>
```